Verpackungsdesign für Dattelkernpulver gesucht
Zielgruppe
Zu uns: Wir sind Nuvo-Lind. Mit unserem Dattelkernpulver bieten wir jedem die Chance die Power der Dattelkerne aktiver in die Ernährung zu integrieren. Neugierigen sowie auch Dattelkennern helfen wir eine ausgewogene Ernährung zu erreichen – dank der sagenumwobenen gesundheitlichen Vorteile der Ajwa-Dattel aus dem Orient. 100% naturbelassen, nicht wärmebehandelt und aus unserer Überzeugung für eine gesunde Ernährung.
Zur Zielgruppe: 50% w/50% m, 30+, aus Deutschland, progressiv und leicht esoterisch, mittleres-höheres Einkommenslevel (EUR 45k+), tendenziell höherer Bildungsgrad, typischerweise 'Verdalis'-Sympathisanten
Aufgabenstellung
Allgemein: Das Produktetikett wird um ein kleines 150g-200g Glas herum angebracht und auf den Deckel ebenfalls ein Rundes Etikett angebracht – verbunden durch ein “Siegel” mit dem zuvorgenannten Hauptetikett.
Vorderseite: Eindeutig erkennbares Logo und Markenname. Auf ersten Blick zu erkennen, dass es sich um Dattelkernpulver handelt ('Dattelkernpulver') inkl. einer Illustration die das leicht erkennen lässt. Deutliche Symbolik: 'Vegan', 'Laktosefrei', “ohne Konservierungsstoffe”, 'Ungezuckert', “Hergestellt in Deutschland”
Seite: Kleiner Blocktext mit 3-4 Zeilen mit kurzer Story zu unserer Überzeugung ('Die Power-Frucht aus 1001 Nacht: Dattelkernpulver von sorgfältig ausgewählten Premium Ajwa-Datteln aus Medina. 100% naturbelassen, nicht wärmebehandelt und aus unserer Überzeugung für ein gesundes Leben.') Zusätzlich eine Verzehrempfehlung ('Als täglicher Begleiter Deiner gesunden Ernährung je morgens einen Teelöffel.')
Rückseite: sehr leicht aufzufindende Zutatenliste sowie ein Dummy für die Nährwerttabelle. Kleiner Hinweis weiter unten auf Rückseite zur Marke (ähnlich wie private label 'kp Hausqualität') mit Kontaktdaten (Webseite, Email, Standort), dass unsere Transparenz und Erreichbarkeit vermittelt.
Oberseite: Label geht mit 'Siegel' bis auf den runden Deckel. Auf Oberseite Logo und schnell identifizierbarer Produktname.
Bitte beachten: Keine Kreuze, keine Dreiecke, nicht zu verspielt.
** Vielen Dank - ich freue mich auf Deinen spannenden Vorschlag! **
Maße:
-> Label: Breite 230mm, Höhe 30mm
-> Deckel: 50mm Druchmesser
-> Lasche vom Deckel zum Label: Breite ca. 10mm-15mm

```html
<!DOCTYPE html>
<html lang="de">
<head>
<meta charset="utf-8">
<title>Nuvo-Lind Dattelkernpulver – Etikett</title>
<link rel="stylesheet" href="https://fonts.googleapis.com/css2?family=Arimo:wght@400;700&family=Lobster&family=Noto+Serif:ital,wght@1,700&display=swap">
<style>
  :root {
    --bg-light: #9a9a9c;
    --bg-dark: #4f4f51;
    --strip-green: #669a00;
    --deep-green: #4f7a00;
    --lime: #9fc43a;
    --lime-text: #d4ec9c;
    --white: #ffffff;
    --paper: #f3f4f5;
    --badge-blue: #1f9ad6;
    --ink: #2b2b2b;
  }
  html, body { margin: 0; padding: 0; width: 1200px; height: 2449px; overflow: hidden; }
  body { background: radial-gradient(ellipse at 50% 55%, var(--bg-light), var(--bg-dark) 75%); }
  svg { display: block; }
  .sans { font-family: "Arimo", Arial, sans-serif; }
  .script { font-family: "Lobster", cursive; }
  .serif-italic { font-family: "Noto Serif", Georgia, serif; font-style: italic; font-weight: 700; }
  .brand-name { font-family: "Arimo", Arial, sans-serif; font-weight: 700; }
  .ring-text { font-family: "Arimo", Arial, sans-serif; font-size: 18px; letter-spacing: 1px; }
</style>
</head>
<body>
<svg class="design" width="1200" height="2449" viewBox="0 0 1200 2449" xmlns="http://www.w3.org/2000/svg">
  <defs>
    <path id="ring-top-2" d="M 718 193 A 67 67 0 0 1 852 193"/>
    <path id="ring-bottom-2" d="M 710 193 A 75 75 0 0 0 860 193"/>
    <path id="ring-top-3" d="M 941 193 A 67 67 0 0 1 1075 193"/>
    <path id="ring-bottom-3" d="M 933 193 A 75 75 0 0 0 1083 193"/>
    <linearGradient id="dates-tone" x1="0" y1="0" x2="1" y2="1">
      <stop offset="0" stop-color="#7a5038"/>
      <stop offset="0.5" stop-color="#3a2418"/>
      <stop offset="1" stop-color="#5a5a5a"/>
    </linearGradient>
  </defs>

  <!-- Lid label with seal tab -->
  <g class="lid-label-tab">
    <rect x="534" y="280" width="62" height="162" fill="var(--lime)"/>
    <circle cx="564" cy="193" r="103" fill="var(--lime)"/>
    <circle cx="564" cy="193" r="88" fill="none" stroke="var(--white)" stroke-width="4"/>
    <circle cx="564" cy="170" r="8" fill="var(--white)"/>
    <text class="brand-name" x="564" y="210" font-size="24" fill="var(--white)" text-anchor="middle">Nuvo-Lind</text>
  </g>

  <!-- Lid label, white variant -->
  <g class="lid-label-white">
    <circle cx="785" cy="193" r="103" fill="var(--white)"/>
    <circle cx="785" cy="193" r="88" fill="none" stroke="var(--lime)" stroke-width="4"/>
    <text class="ring-text" fill="var(--lime)" text-anchor="middle"><textPath href="#ring-top-2" startOffset="50%">Dattelkernpulver</textPath></text>
    <text class="ring-text" fill="var(--lime)" text-anchor="middle"><textPath href="#ring-bottom-2" startOffset="50%">Premium Ajwa</textPath></text>
    <text class="brand-name" x="785" y="201" font-size="22" fill="var(--badge-blue)" text-anchor="middle">Nuvo-Lind</text>
  </g>

  <!-- Lid label, green variant -->
  <g class="lid-label-green">
    <circle cx="1008" cy="193" r="103" fill="var(--lime)"/>
    <circle cx="1008" cy="193" r="88" fill="none" stroke="var(--white)" stroke-width="4"/>
    <text class="ring-text" fill="var(--white)" text-anchor="middle"><textPath href="#ring-top-3" startOffset="50%">Dattelkernpulver</textPath></text>
    <text class="ring-text" fill="var(--white)" text-anchor="middle"><textPath href="#ring-bottom-3" startOffset="50%">Premium Ajwa</textPath></text>
    <circle cx="1008" cy="160" r="8" fill="var(--white)"/>
    <text class="brand-name" x="1008" y="205" font-size="24" fill="var(--white)" text-anchor="middle">Nuvo-Lind</text>
  </g>

  <!-- Main wrap label -->
  <g class="wrap-label">
    <!-- Back panel -->
    <g class="back-panel">
      <rect x="88" y="440" width="266" height="123" fill="var(--strip-green)"/>
      <text class="sans" x="107" y="463" font-size="10" font-weight="700" fill="var(--lime-text)">zutaten :</text>
      <text class="sans" x="107" y="475" font-size="8.5" fill="var(--lime-text)">Vegan, Laktosefrei,</text>
      <text class="sans" x="107" y="485" font-size="8.5" fill="var(--lime-text)">ohne Konservierungsstoffe, Ungezuckert,</text>
      <text class="sans" x="107" y="500" font-size="8.5" font-weight="700" fill="var(--lime-text)">Ursprung : Deutschland</text>
      <line x1="107" y1="508" x2="265" y2="508" stroke="var(--lime-text)" stroke-width="1" stroke-dasharray="5 3"/>
      <g class="diet-icons" fill="none" stroke="var(--lime-text)" stroke-width="1.2">
        <path d="M120 545 q8 -4 12 -16 M126 531 q6 2 4 10 M118 532 q4 6 8 5"/>
        <circle cx="155" cy="537" r="10"/><path d="M149 541 q6 -10 12 -6 q-4 8 -12 6"/>
        <circle cx="185" cy="537" r="10"/><line x1="178" y1="530" x2="192" y2="544"/><rect x="182" y="531" width="6" height="12" rx="2"/>
        <circle cx="215" cy="537" r="10"/><line x1="208" y1="530" x2="222" y2="544"/><path d="M212 543 l6 -12"/>
        <circle cx="245" cy="537" r="10"/><line x1="238" y1="530" x2="252" y2="544"/><path d="M241 541 q4 -9 8 -8"/>
      </g>
      <g class="nutrition-table">
        <rect x="277" y="449" width="70" height="105" fill="none" stroke="var(--white)" stroke-width="1"/>
        <text class="sans" x="280" y="459" font-size="7" font-weight="700" fill="var(--white)">Nutrition Facts</text>
        <line x1="280" y1="462" x2="344" y2="462" stroke="var(--white)"/>
        <g class="sans" font-size="3.2" fill="var(--white)">
          <text x="280" y="467">Serving Size 5 g</text>
          <text x="280" y="471">Servings 40</text>
          <text x="280" y="478" font-weight="700">Amount Per Serving</text>
          <text x="280" y="484">Calories 18</text>
          <text x="280" y="490" font-weight="700">Total Fat 0.4 g</text>
          <text x="284" y="496">Sodium 2 mg</text>
          <text x="280" y="502" font-weight="700">Total Carbohydrate 4 g</text>
          <text x="284" y="508">Dietary Fiber 3 g</text>
          <text x="284" y="514">Sugars 0 g</text>
          <text x="280" y="520" font-weight="700">Protein 0.3 g</text>
          <text x="284" y="526">Vitamin A 0%</text>
          <text x="284" y="532">Vitamin C 0%</text>
          <text x="284" y="538">Iron 2%</text>
        </g>
        <g stroke="var(--white)" stroke-width="0.4">
          <line x1="280" y1="474" x2="344" y2="474"/><line x1="280" y1="486" x2="344" y2="486"/>
          <line x1="280" y1="498" x2="344" y2="498"/><line x1="280" y1="516" x2="344" y2="516"/>
          <line x1="280" y1="522" x2="344" y2="522"/><line x1="280" y1="540" x2="344" y2="540"/>
          <line x1="280" y1="546" x2="344" y2="546"/>
        </g>
      </g>
    </g>

    <!-- Front panel -->
    <g class="front-panel">
      <rect x="354" y="440" width="421" height="123" fill="var(--paper)"/>
      <path class="header-swoosh" d="M 560 482 C 620 464, 640 444, 690 444 L 775 444 L 775 485 C 700 480, 620 476, 560 482 Z" fill="var(--lime)"/>
      <path d="M 360 492 C 470 502, 560 490, 610 472" fill="none" stroke="var(--strip-green)" stroke-width="2"/>
      <circle cx="392" cy="467" r="12" fill="var(--badge-blue)"/>
      <text class="brand-name" x="412" y="474" font-size="20" fill="var(--strip-green)">Nuvo-Lind</text>
      <text class="serif-italic" x="758" y="464" font-size="11.5" fill="var(--deep-green)" text-anchor="end">Gesunde Ernährung</text>
      <text class="serif-italic" x="758" y="478" font-size="11.5" fill="var(--deep-green)" text-anchor="end">Premium Ajwa</text>
      <text class="script" x="377" y="540" font-size="27" fill="var(--strip-green)">Dattelkernpulver</text>
      <rect class="product-photo" x="570" y="487" width="140" height="68" rx="30" fill="url(#dates-tone)" role="img" aria-label="Foto: Ajwa-Datteln auf einer Schale"/>
      <g class="badge-100">
        <circle cx="720" cy="512" r="28" fill="var(--badge-blue)"/>
        <circle cx="720" cy="512" r="24" fill="none" stroke="var(--white)" stroke-width="1.5"/>
        <text class="sans" x="721" y="508" font-size="9" font-weight="700" fill="var(--white)" text-anchor="middle">Orient.</text>
        <text class="sans" x="720" y="522" font-size="14" font-weight="700" fill="var(--white)" text-anchor="middle">100%</text>
      </g>
      <text class="sans" x="763" y="557" font-size="14" font-weight="700" fill="var(--ink)" text-anchor="end">200 g</text>
    </g>

    <!-- Side panel -->
    <g class="side-panel">
      <rect x="775" y="440" width="265" height="123" fill="var(--strip-green)"/>
      <rect x="783" y="450" width="244" height="72" rx="5" fill="none" stroke="var(--lime-text)" stroke-width="1.5"/>
      <g class="sans story-text" font-size="7.4" fill="var(--white)">
        <text x="795" y="468">'Die Power-Frucht aus 1001 Nacht: Dattelkernpulver von</text>
        <text x="795" y="477">sorgfältig ausgewählten Premium Ajwa-Datteln aus Medina.</text>
        <text x="795" y="486">100% naturbelassen, nicht wärmebehandelt und aus unserer</text>
        <text x="795" y="495">Überzeugung für ein gesundes Leben.') Zusätzlich eine</text>
        <text x="795" y="504">Verzehrempfehlung ('Als täglicher Begleiter Deiner gesunden</text>
        <text x="795" y="513">Ernährung je morgens einen Teelöffel.')</text>
      </g>
      <g class="sans contact" font-size="8" fill="var(--lime-text)">
        <text x="792" y="537">your place</text>
        <text x="792" y="545">zip code</text>
        <text x="792" y="553">country</text>
        <text x="845" y="543">www.yourwebsite.com</text>
        <text x="845" y="552">yourmail@.com</text>
      </g>
    </g>
  </g>
</svg>
</body>
</html>
```